Hybrid Repair & Maintenance Services for Velmar & Brisk (Need a Postcard Design)

We need a 5 x 7 postcard, to be handed out...Not Mailed. Both sides would have content. We have the least costly options to take care of a Velmar and Brisk Hybrid batteries. Also Hybrid Repair & Maintenance Services (the large pack) Please feel free to use whatever you feel would make this pop (if possible) :) I have attached a one page attempt to bring content to you.

Target Market(s)

Velmar and Brisk Hybrid Consumers

```html
<!DOCTYPE html>
<html lang="en">
<head>
<meta charset="utf-8">
<title>Hybrid Repair Postcard – Velmar &amp; Brisk</title>
<link href="https://fonts.googleapis.com/css2?family=Roboto+Condensed:wght@400;700&family=Roboto:ital,wght@1,400&display=swap" rel="stylesheet">
<style>
  :root {
    --backdrop: #6b6b6d;
    --paper: #ffffff;
    --navy: #233b8e;
    --red: #d3222a;
    --yellow: #f5ec1c;
    --ink: #1d1d1d;
    --rule: #8a8a8a;
  }
  * { box-sizing: border-box; margin: 0; padding: 0; }
  html, body { width: 1200px; height: 970px; overflow: hidden; background: var(--backdrop); }
  .postcard {
    position: absolute; left: 80px; top: 85px; width: 1042px; height: 801px;
    background: var(--paper); color: var(--ink);
    font-family: "Roboto Condensed", "Arial Narrow", sans-serif;
  }
  .headline {
    position: absolute; top: 28px; left: 0; width: 100%; text-align: center;
    font-weight: 700; font-size: 45px; color: var(--red); letter-spacing: 0.2px;
  }
  .intro-band {
    position: absolute; top: 87px; left: 0; width: 100%; height: 171px;
    background: var(--navy); text-align: center; color: var(--paper);
  }
  .intro-band h2 {
    margin-top: 14px; font-weight: 700; font-size: 32px; color: var(--yellow);
  }
  .intro-band p {
    margin: 4px auto 0; width: 1010px;
    font-family: "Roboto", Arial, sans-serif; font-style: italic; font-size: 22.5px; line-height: 31.5px;
  }
  .services { position: absolute; left: 42px; top: 285px; width: 420px; }
  .services h3 { font-weight: 700; font-size: 23px; line-height: 30px; color: var(--navy); }
  .services ul { list-style: none; margin-top: 16px; }
  .services li {
    position: relative; padding-left: 27px; margin-bottom: 16px;
    font-size: 21px; line-height: 26px; color: var(--ink);
  }
  .services li svg { position: absolute; left: 0; top: 6px; width: 20px; height: 16px; }
  .column-rule { position: absolute; left: 483px; top: 285px; width: 1px; height: 442px; background: var(--rule); }
  .battery { position: absolute; left: 500px; top: 282px; width: 528px; text-align: center; }
  .battery h3 { font-weight: 700; font-size: 29px; line-height: 37px; color: var(--red); }
  .battery .signs { font-weight: 700; font-size: 23px; margin-top: 3px; color: var(--ink); }
  .battery .note {
    margin: 20px auto 0; width: 520px;
    font-family: "Roboto", Arial, sans-serif; font-style: italic; font-size: 19.5px; line-height: 26px;
  }
  .battery .offer { margin-top: 22px; font-family: Arial, "Roboto", sans-serif; font-weight: 700; font-size: 30px; line-height: 39px; }
  .offer .navy { color: var(--navy); }
  .offer .red { color: var(--red); }
  .battery .options { margin-top: 20px; font-weight: 700; font-size: 25px; color: var(--red); }
  .options .star { color: var(--navy); font-size: 18px; vertical-align: 2px; }
  .closing-band {
    position: absolute; bottom: 0; left: 0; width: 100%; height: 57px; background: var(--navy);
    text-align: center; line-height: 57px; font-weight: 700; font-size: 23.5px; color: var(--yellow);
  }
</style>
</head>
<body>
<main class="postcard">
  <h1 class="headline">FLEET PRICING FOR THE SINGLE CAR OWNER</h1>

  <section class="intro-band">
    <h2>Hybrid Repair &amp; Maintenance Services for Velmar &amp; Brisk</h2>
    <p>Underperforming vehicle? To maintain fuel efficiency, your combustion engine, drive motor, generator and Hybrid battery pack must be in balance with each other. If one system is stressed, the other components suffer, possibly causing unrecoverable damage.</p>
  </section>

  <section class="services">
    <h3>A Complete Hybrid Vehicle and Hybrid Battery Maintenance &amp; Repair</h3>
    <ul>
      <li><svg viewBox="0 0 20 16"><path d="M2 8 L7.5 13.5 L18 3" fill="none" stroke="#d3222a" stroke-width="4" stroke-linecap="round" stroke-linejoin="round"/></svg>Complete computer diagnostic test. Cutting-edge technology for fast and accurate diagnosis of issues.</li>
      <li><svg viewBox="0 0 20 16"><path d="M2 8 L7.5 13.5 L18 3" fill="none" stroke="#d3222a" stroke-width="4" stroke-linecap="round" stroke-linejoin="round"/></svg>Electrical systems inspection. To identify abnormalities in systems and connections.</li>
      <li><svg viewBox="0 0 20 16"><path d="M2 8 L7.5 13.5 L18 3" fill="none" stroke="#d3222a" stroke-width="4" stroke-linecap="round" stroke-linejoin="round"/></svg>Wire and cable check. Outside sheath of cables inspected for cuts and tears.</li>
      <li><svg viewBox="0 0 20 16"><path d="M2 8 L7.5 13.5 L18 3" fill="none" stroke="#d3222a" stroke-width="4" stroke-linecap="round" stroke-linejoin="round"/></svg>Complete vehicle inspection. We look at all conventional systems as well as hybrid-specific systems, and let you know what needs attention now, and what may need attention down the road.</li>
    </ul>
  </section>

  <div class="column-rule"></div>

  <section class="battery">
    <h3>2 KEY INDICATORS YOUR HYBRID<br>BATTERY NEEDS SERVICE</h3>
    <p class="signs">Loss of Gas Mileage or Lack of Power</p>
    <p class="note">Because your HEV’s service light will generally not turn on when your battery starts to underperform, it’s important that you’re aware of your vehicle’s gas mileage and performance, therefore showing you if a service is in order.</p>
    <p class="offer"><span class="navy">CREST AUTO offers a</span><br><span class="red">Full Range of Battery Options</span><br><span class="navy">for your Hybrid Vehicle Needs</span></p>
    <p class="options">CONDITIONED <span class="star">★</span> REBUILT <span class="star">★</span> REMANUFACTURED</p>
  </section>

  <footer class="closing-band">WE LOOK FORWARD TO YOUR CALL SO WE CAN ANSWER ANY QUESTIONS YOU MAY HAVE</footer>
</main>
</body>
</html>
```